Manufacturer of prepared Persian ready meals needs a product concept design

I need a product concept design for a new company based in the UK called 'Velmora Foods Ltd'.
The winner will potentially be selected to produce prototype designs for our other products.
For this project, the product will be called "Ghormeh Sabzi". This needs to be on the design to let consumers know what it is.
Whilst still in the concept stage, the aim of the company is to produce refrigerated microwaveable / oven Persian ready meal for retail supermarket consumers, and may also have an online platform for direct to consumer sales.
I have provided quite a few competitor examples of products.
I would like the product in a black or clear round bowl. It will be split into two sections (Half stew / Half rice) by the sleeve, which you are designing. I would like the food to be visible on either side of the label, so the consumer knows what they are eating.
The logo is provided within the file attachments and needs to be on prominent display on the pouch.
The mission for Velmora Foods Ltd brand is:
"Bringing 2,500 years of scented history to your table".
This needs to be present on the sleeve.
The product needs to represent the ethnicity of the brand throughout the design, and the same font to be used throughout.
Persian architecture was filled with a wide range of vibrant colours and has been engineered to stand the test of time, so I would like that to be incorporated into the product design (see attached examples of Persian geometry).
Alternatively Persian carpets are world renowned for their quality, so examples of this could be displayed on the packaging.
These will have to be artistically interpreted to avoid potential copyright; I am looking for individual artistic design.
It needs to represent a super quality, royalty & decadence throughout, and stand out on the shelves to the consumer above all the other competitor products.
To comply with food standards, the sleeve must have a nutritional label on display. I have attached a generic example for you to use. You may create your own representation of it.
Ghormeh Sabzi is a natural source of fibre, high in protein, gluten and dairy free, so I would like this displayed on the sleeve, as well as the the words:
- Traditionally rich in aromatic herbs, tender slow cooked lamb, red kidney beans & dried limes
- One of the oldest dishes in Persian history
You can find pictures of the food provided in the files. Note, these are not my pictures, but give you an idea of what will be provided inside.
Some designers have uploaded the same design up to 5 times, others twice. Only 18 have been uploaded, but it says 20, so I think 2 have been removed?

```html
<!DOCTYPE html>
<html lang="en">
<head>
<meta charset="utf-8">
<title>Velmora Foods – Ghormeh Sabzi sleeve</title>
<link href="https://fonts.googleapis.com/css2?family=Archivo:wdth,wght@125,800;125,900&family=Barlow+Condensed:ital,wght@0,400;0,500;1,600&display=swap" rel="stylesheet">
<style>
  :root {
    --backdrop: #7abdad;
    --sleeve-green: #0f4538;
    --brand-yellow: #f2ee5a;
    --pill-teal: #1a8a6e;
    --ellipse-teal: #1f8a70;
    --white: #ffffff;
    --energy: #22b3d6;
    --saturates: #a5c33a;
    --salt: #f2b51d;
    --sugar: #e42b38;
    --fat: #f9b81c;
  }
  * { margin: 0; padding: 0; box-sizing: border-box; }
  html, body { width: 1200px; height: 1200px; overflow: hidden; }
  body { background: var(--backdrop); position: relative; font-family: "Barlow Condensed", sans-serif; }

  .sleeve {
    position: absolute; left: 357px; top: 114px; width: 486px; height: 972px;
    background: var(--sleeve-green); overflow: hidden;
    box-shadow: 8px 14px 30px rgba(0, 40, 30, 0.35);
  }
  .centered { position: absolute; left: 0; right: 0; text-align: center; }

  .brand-dot { position: absolute; left: 231px; top: 54px; width: 24px; height: 24px; border-radius: 50%; background: var(--brand-yellow); }
  .brand-name { top: 118px; color: var(--white); font-weight: 500; font-size: 30px; letter-spacing: 9px; line-height: 1; padding-left: 9px; }
  .brand-sub { top: 152px; color: var(--white); font-weight: 500; font-size: 14px; letter-spacing: 6px; line-height: 1; padding-left: 6px; }

  .product-ellipse { position: absolute; left: 83px; top: 241px; }
  .product-title {
    font-family: "Archivo", sans-serif; font-stretch: 125%; font-weight: 900;
    color: var(--brand-yellow); line-height: 1; letter-spacing: -1px;
  }
  .title-ghormeh { top: 186px; font-size: 62px; }
  .title-sabzi { top: 246px; font-size: 62px; }

  .mission { top: 332px; color: var(--white); font-size: 19px; }
  .mission em { color: var(--brand-yellow); font-weight: 600; }

  .claims { position: absolute; top: 392px; left: 55px; display: flex; gap: 6px; }
  .claim {
    height: 26px; border: 1.5px solid var(--brand-yellow); border-radius: 13px;
    background: var(--pill-teal); color: var(--white); font-size: 13px;
    display: flex; align-items: center; justify-content: center;
  }
  .claim-fibre { width: 137px; }
  .claim-free { width: 128px; }
  .claim-protein { width: 98px; }

  .description { top: 440px; color: var(--white); font-size: 14.5px; line-height: 18px; }
  .wave { position: absolute; left: 59px; top: 494px; }

  .heritage {
    top: 530px; font-family: "Archivo", sans-serif; font-stretch: 125%; font-weight: 900;
    font-size: 18px; line-height: 23px; color: var(--white); letter-spacing: -0.6px;
  }
  .heritage span { color: var(--brand-yellow); }

  .meal-art { position: absolute; left: 0; top: 590px; }

  .nutrition { position: absolute; top: 872px; left: 96px; display: flex; gap: 10px; }
  .nutrient {
    width: 51px; height: 76px; border-radius: 6px; border: 1.5px solid var(--white);
    overflow: hidden; color: var(--white); text-align: center; position: relative;
  }
  .nutrient-head { height: 15px; font-size: 6px; font-weight: 500; line-height: 15px; background: rgba(255,255,255,0.12); border-bottom: 1px solid var(--white); text-transform: uppercase; }
  .nutrient-value { font-size: 10.5px; line-height: 11px; margin-top: 3px; }
  .nutrient-ri {
    position: absolute; left: 4px; right: 4px; bottom: 4px; height: 18px; border-radius: 9px;
    background: #fdfbf5; color: #444; font-size: 10px; line-height: 18px;
  }
  .energy { background: var(--energy); }
  .saturates { background: var(--saturates); }
  .salt { background: var(--salt); }
  .sugar { background: var(--sugar); }
  .fat { background: var(--fat); }
</style>
</head>
<body>
  <main class="sleeve">
    <div class="brand-dot"></div>
    <p class="centered brand-name">VELMORA</p>
    <p class="centered brand-sub">FOODS</p>

    <svg class="product-ellipse" width="322" height="76" viewBox="0 0 322 76">
      <ellipse cx="161" cy="38" rx="159" ry="36" fill="none" stroke="var(--ellipse-teal)" stroke-width="1.5"/>
    </svg>
    <h1 class="centered product-title title-ghormeh">GHORMEH</h1>
    <h1 class="centered product-title title-sabzi">SABZI</h1>

    <p class="centered mission">Bringing <em>2,500 years</em> of scented history to your table</p>

    <ul class="claims">
      <li class="claim claim-fibre">Natural Source Of Fibre</li>
      <li class="claim claim-free">Gluten And Dairy Free</li>
      <li class="claim claim-protein">High In Protein</li>
    </ul>

    <p class="centered description">Traditionally rich in aromatic herbs, tender slow cooked lamb,<br>red kidney beans &amp; dried limes</p>

    <svg class="wave" width="368" height="12" viewBox="0 0 368 12">
      <path d="M0 6 Q15 0 30 6 T60 6 T90 6 T120 6 T150 6 T180 6 T210 6 T240 6 T270 6 T300 6 T330 6 T360 6 L368 4" fill="none" stroke="var(--brand-yellow)" stroke-width="1.6"/>
    </svg>

    <h2 class="centered heritage">ONE OF THE OLDEST DISHES IN<br><span>PERSIAN HISTORY</span></h2>

    <svg class="meal-art" width="486" height="382" viewBox="0 0 486 382">
      <defs>
        <radialGradient id="stew" cx="0.5" cy="0.6" r="0.7">
          <stop offset="0" stop-color="#4f5a2a"/>
          <stop offset="0.6" stop-color="#3b4a22"/>
          <stop offset="0.85" stop-color="#8a8a3a"/>
          <stop offset="1" stop-color="#d9d6c8"/>
        </radialGradient>
      </defs>
      <path d="M0 146 C90 70 170 30 239 23 C320 15 420 60 486 140 L486 382 L0 382 Z" fill="var(--brand-yellow)"/>
      <path role="img" aria-label="Photo of a bowl of ghormeh sabzi stew with lamb, kidney beans and herbs" d="M0 168 C90 95 170 60 245 52 C330 45 420 80 486 150 L486 382 L0 382 Z" fill="url(#stew)"/>
    </svg>

    <section class="nutrition" aria-label="Nutrition per pack">
      <div class="nutrient energy"><div class="nutrient-head">Energy</div><div class="nutrient-value">1046 kJ<br>250 kcal</div><div class="nutrient-ri">13%</div></div>
      <div class="nutrient saturates"><div class="nutrient-head">Saturates</div><div class="nutrient-value">1.3 g<br>Low</div><div class="nutrient-ri">7%</div></div>
      <div class="nutrient salt"><div class="nutrient-head">Salt</div><div class="nutrient-value">0.9 g<br>Medium</div><div class="nutrient-ri">15%</div></div>
      <div class="nutrient sugar"><div class="nutrient-head">Sugar</div><div class="nutrient-value">34 g<br>High</div><div class="nutrient-ri">38%</div></div>
      <div class="nutrient fat"><div class="nutrient-head">Fat</div><div class="nutrient-value">3.0 g<br>Low</div><div class="nutrient-ri">4%</div></div>
    </section>
  </main>
</body>
</html>
```